Rebrand of 3 bottle labels for nail polish brand

The task is to make a rebranding of our current gel nail polish bottle design. We have become one of the leading european nail polish brand, so we want to improve the quality of the label design to a more scandinavian and minimalistic bottle design, which stille has to be recognisable and unique.

We have attached a more detailed description of the rebranding instructions for our gel polish bottles called "bottle task".
Updates

The Labels should not be just Black and White as stated. But should be mainly Black and White and then some of our color as explained in the uploaded file.

Target Market(s)

Girls and women age 18-55 Northern Europe

Industry/Entity Type

Cosmetic/ Nail Gel Polish

Colors

Designer to choose only greyscale colors for use in the design.

Requirements
Must have
• See attched design instruction
Nice to have
• Moderne, Minimalist, Recognizable and Unique look
Should not have
• Too many elements, too busy design

```html
<!DOCTYPE html>
<html lang="en">
<head>
<meta charset="utf-8">
<title>Lumevi gel polish labels</title>
<link rel="stylesheet" href="https://fonts.googleapis.com/css2?family=Roboto:wght@300;400;700&family=Roboto+Condensed:wght@400;700&display=swap">
<style>
  :root{
    --ink:#000;
    --pattern-a:#0a0a0a;
    --pattern-b:#171717;
    --white:#fff;
    --rose:#c49a90;
    --rose-deep:#8e6a63;
    --rose-text:#d9a89c;
    --lemon:#f1f5c4;
    --lime:#c9e29a;
    --leaf:#5e9a60;
    --paper:#fff;
    --hair:#444;
  }
  *{margin:0;padding:0;box-sizing:border-box}
  html,body{width:931px;height:1200px;overflow:hidden;background:var(--paper)}
  body{position:relative;font-family:"Roboto",Arial,sans-serif;color:var(--white)}

  .label{position:absolute;left:30px;background:var(--ink);overflow:hidden}
  .label--color{top:70px;width:871px;height:232px;border-radius:28px;border:1px solid #c33}
  .label--base{top:370px;width:871px;height:232px;border-bottom:1px solid #c33}
  .label--remover{top:670px;width:822px;height:351px}

  .pattern{position:absolute;inset:0;background:linear-gradient(135deg,var(--pattern-a),var(--pattern-b) 50%,var(--pattern-a))}

  .front{position:absolute;left:0;top:0;width:470px;height:100%;text-align:center}
  .brand{position:absolute;left:0;width:100%;font-weight:300;font-size:50px;letter-spacing:1px;line-height:1}
  .brand sup{font-size:10px;vertical-align:top;position:relative;top:4px;margin-left:2px}
  .label--color .brand,.label--base .brand{top:28px}

  .product-band{position:absolute;left:0;top:88px;width:470px;height:29px;background:var(--rose);
    font-family:"Roboto Condensed",Arial,sans-serif;font-weight:700;font-size:21px;color:#1a1a1a;line-height:29px}
  .product-title{position:absolute;left:0;width:100%;top:88px;font-family:"Roboto Condensed",Arial,sans-serif;font-weight:700;font-size:21px;line-height:29px}
  .product-title .tab{display:inline-block;width:14px;height:24px;background:var(--rose);vertical-align:middle;margin:0 12px}
  .soak{position:absolute;left:0;width:100%;top:122px;font-family:"Roboto Condensed",Arial,sans-serif;font-size:11.5px}

  .shade{position:absolute;left:0;width:100%;top:141px;height:40px}
  .shade .vegan{position:absolute;left:186px;top:6px;width:22px;height:30px;border:1.5px solid var(--leaf);border-radius:50% 50% 50% 50%/60% 60% 40% 40%}
  .shade .chip{position:absolute;left:218px;top:0;width:54px;height:40px;border-radius:50%;color:#111;font-size:21px;font-weight:400;line-height:40px}
  .chip--lemon{background:var(--lemon)}
  .chip--lime{background:var(--lime)}
  .shade-name{position:absolute;left:0;width:100%;top:182px;font-size:15px;font-weight:300}
  .pointer{position:absolute;left:234px;top:200px;width:0;height:0;border-left:10px solid transparent;border-right:10px solid transparent;border-top:10px solid var(--lime)}
  .origin{position:absolute;left:0;width:100%;top:212px;font-size:9.5px}

  .ingredients{position:absolute;top:16px;height:205px;left:482px;writing-mode:vertical-rl;transform:rotate(180deg);
    font-size:8.3px;line-height:1.05;color:var(--white)}
  .ingredients b{font-weight:700}

  .info{position:absolute;top:20px;width:122px;font-size:8px;line-height:1.12}
  .info h4{font-size:8.5px;font-weight:700;margin-top:0}
  .info h4+p{margin-bottom:6px}
  .info .flag{position:absolute;left:-20px;top:-2px;width:14px;height:14px;border-radius:50%}
  .flag--dk{background:linear-gradient(#000 33%,#d00 33% 66%,#fc0 66%)}
  .flag--us{background:repeating-linear-gradient(#c00 0 2px,#fff 2px 4px);box-shadow:inset 6px 6px 0 -1px #2a3b8f}
  .info--da{left:560px}
  .info--en{left:705px}

  .footer{position:absolute;left:550px;width:290px}
  .address{font-size:7.6px;text-align:right;padding-bottom:3px}
  .web{font-size:14px;color:var(--rose-text);text-align:right}
  .made{font-size:10.5px;font-weight:700;text-align:right;margin-top:2px}
  .size{position:absolute;right:0;width:82px;height:17px;background:var(--rose);color:#111;font-size:10px;line-height:17px;text-align:center}
  .icons{position:absolute;left:2px;display:flex;gap:12px;align-items:center}
  .icons svg{width:22px;height:22px}
  .label--color .footer,.label--base .footer{top:166px}
  .label--color .size,.label--base .size{top:49px}
  .label--color .icons,.label--base .icons{top:34px}

  /* remover */
  .label--remover .front{width:470px}
  .brand-box{position:absolute;left:141px;top:14px;width:192px;height:88px;background:linear-gradient(120deg,var(--rose-deep),var(--rose) 55%,var(--rose-deep))}
  .label--remover .brand{top:28px;left:141px;width:192px;color:#1a1a1a;font-size:50px}
  .remover-title{position:absolute;left:0;width:470px;top:112px;font-family:"Roboto Condensed",Arial,sans-serif;font-weight:700;font-size:23px;line-height:30px}
  .drop{position:absolute;left:200px;top:178px;width:76px;height:98px}
  .drop span{position:absolute;left:0;top:14px;width:76px;text-align:center;color:#000;font-size:38px;font-weight:400}
  .label--remover .vegan{position:absolute;left:172px;top:232px;width:28px;height:40px;border:1.5px solid var(--leaf);border-radius:50% 50% 50% 50%/60% 60% 40% 40%}
  .volume{position:absolute;left:0;width:470px;top:284px;font-size:13px}
  .label--remover .origin{top:308px;width:470px}
  .label--remover .ingredients{left:490px;top:30px;height:290px}
  .label--remover .info{top:34px}
  .label--remover .info--da{left:556px;width:118px}
  .label--remover .info--en{left:695px;width:120px}
  .label--remover .footer{left:530px;top:270px;width:285px}
  .label--remover .size{top:49px}
  .label--remover .icons{top:32px}
  .rule{position:absolute;left:540px;top:263px;width:272px;border-top:1px solid var(--hair)}
</style>
</head>
<body>

<svg width="0" height="0" style="position:absolute" aria-hidden="true">
  <defs>
    <symbol id="icon-jar" viewBox="0 0 24 24"><rect x="3" y="9" width="18" height="11" fill="none" stroke="#fff" stroke-width="1.5"/><path d="M3 8l17-4" stroke="#fff" stroke-width="1.5"/><text x="12" y="18" font-size="6" fill="#fff" text-anchor="middle" font-family="Arial">24M</text></symbol>
    <symbol id="icon-recycle" viewBox="0 0 24 24"><path d="M12 3l4 7H8z M4 19l4-7 4 7z M20 19h-8l4-7z" fill="#fff"/></symbol>
    <symbol id="icon-warning" viewBox="0 0 24 24"><path d="M12 2l10 10-10 10L2 12z" fill="none" stroke="#fff" stroke-width="1.5"/><rect x="11" y="7" width="2" height="7" fill="#fff"/><circle cx="12" cy="17" r="1.2" fill="#fff"/></symbol>
    <symbol id="icon-lamp" viewBox="0 0 24 24"><path d="M5 8a7 7 0 0 1 13 0v3H5z" fill="#fff"/><path d="M7 14l-2 5M12 14v6M17 14l2 5" stroke="#fff" stroke-width="1.5"/></symbol>
  </defs>
</svg>

<!-- Color coat -->
<section class="label label--color" aria-label="Color coat label">
  <div class="pattern" role="img" aria-label="Faint grey leaf outline pattern across the label"></div>
  <div class="front">
    <div class="brand">Lumevi<sup>™</sup></div>
    <div class="product-band">COLOR COAT</div>
    <div class="soak">SOAK OFF UV/LED</div>
    <div class="shade"><span class="vegan"></span><span class="chip chip--lemon">212</span></div>
    <div class="shade-name">LEMON GELATO</div>
    <div class="pointer" style="border-top-color:var(--lemon)"></div>
    <div class="origin">Made in Europe</div>
  </div>
  <p class="ingredients"><b>INGREDIENTS:</b> Acrylates Copolymer, Acrylated Aliphatic Urethane, Cellulose Acetate Butanoate, Dimethicone, Ceresine, wax, Pigment Red, Carbon Black, Titanium dioxide, CI 77891</p>
  <div class="info info--da"><span class="flag flag--dk"></span>
    <h4>ANVENDELSE:</h4><p>Lumevi Farver skal påføres i tynde lag og hærdes i en af vores Lumevi Lamper.</p>
    <h4>ADVARSEL:</h4><p>Opbevar utilgængeligt for børn. Stop din behandling, hvis produktet forudsager irritation. Undgå direkte sollys eller udsættelse for LED eller UV.</p>
  </div>
  <div class="info info--en"><span class="flag flag--us"></span>
    <h4>DIRECTIONS FOR USE:</h4><p>Lumevi Color Coat must be applied in thin layers and cured in one of our Lumevi Lamps.</p>
    <h4>CAUTION:</h4><p>Keep out of reach of children. Discontinue use if irritation occurs. Avoid direct sunlight or extreme exposure to LED or UV Light.</p>
  </div>
  <div class="footer">
    <p class="address">Nordhaven Studio ApS - Fjordvej 12, 2450 Copenhagen, Denmark</p>
    <p class="web">lumevi.example</p>
    <p class="made">Made in Germany</p>
    <div class="icons"><svg><use href="#icon-jar"/></svg><svg><use href="#icon-recycle"/></svg><svg><use href="#icon-warning"/></svg><svg><use href="#icon-lamp"/></svg></div>
    <div class="size">15ml e 0.5oz</div>
  </div>
</section>

<!-- Base coat -->
<section class="label label--base" aria-label="Base coat label">
  <div class="pattern" role="img" aria-label="Faint grey leaf outline pattern across the label"></div>
  <div class="front">
    <div class="brand">Lumevi<sup>™</sup></div>
    <div class="product-title"><span class="tab"></span>BASE COAT<span class="tab"></span></div>
    <div class="soak">SOAK OFF UV/LED</div>
    <div class="shade"><span class="vegan"></span><span class="chip chip--lime">01</span></div>
    <div class="shade-name">FLEXIBLE</div>
    <div class="pointer"></div>
    <div class="origin">Made in Europe</div>
  </div>
  <p class="ingredients"><b>INGREDIENTS:</b> Acrylates Copolymer, Acrylated Aliphatic Urethane, Cellulose Acetate Butanoate, Dimethicone, Ceresine, wax, Pigment Red, Carbon Black, Titanium dioxide, CI 77891</p>
  <div class="info info--da"><span class="flag flag--dk"></span>
    <h4>ANVENDELSE:</h4><p>Lumevi Farver skal påføres i tynde lag og hærdes i en af vores Lumevi Lamper.</p>
    <h4>ADVARSEL:</h4><p>Opbevar utilgængeligt for børn. Stop din behandling, hvis produktet forudsager irritation. Undgå direkte sollys eller udsættelse for LED eller UV.</p>
  </div>
  <div class="info info--en"><span class="flag flag--us"></span>
    <h4>DIRECTIONS FOR USE:</h4><p>Lumevi Color Coat must be applied in thin layers and cured in one of our Lumevi Lamps.</p>
    <h4>CAUTION:</h4><p>Keep out of reach of children. Discontinue use if irritation occurs. Avoid direct sunlight or extreme exposure to LED or UV Light.</p>
  </div>
  <div class="footer">
    <p class="address">Nordhaven Studio ApS - Fjordvej 12, 2450 Copenhagen, Denmark</p>
    <p class="web">lumevi.example</p>
    <p class="made">Made in Germany</p>
    <div class="icons"><svg><use href="#icon-jar"/></svg><svg><use href="#icon-recycle"/></svg><svg><use href="#icon-warning"/></svg><svg><use href="#icon-lamp"/></svg></div>
    <div class="size">15ml e 0.5oz</div>
  </div>
</section>

<!-- Remover -->
<section class="label label--remover" aria-label="Gel polish remover label">
  <div class="pattern" role="img" aria-label="Faint grey leaf outline pattern across the label"></div>
  <div class="front">
    <div class="brand-box"></div>
    <div class="brand">Lumevi<sup>™</sup></div>
    <div class="remover-title">GEL POLISH<br>REMOVER</div>
    <span class="vegan"></span>
    <div class="drop">
      <svg viewBox="0 0 76 98" width="76" height="98"><path d="M38 2C17 2 2 18 2 38c0 22 20 36 36 58 16-22 36-36 36-58C74 18 59 2 38 2z" fill="#fff"/></svg>
      <span>12</span>
    </div>
    <div class="volume">120ml e 04 fl.oz</div>
    <div class="origin">Made in Europe</div>
  </div>
  <p class="ingredients"><b>INGREDIENTS:</b> Acrylates Copolymer, Acrylated Aliphatic Urethane, Cellulose Acetate Butanoate, Dimethicone, Ceresine, wax, Pigment Red, Carbon Black, Titanium dioxide, CI 77891</p>
  <div class="info info--da"><span class="flag flag--dk"></span>
    <h4>ANVENDELSE:</h4><p>For at fjerne Lumevi, skal du væde en fnugfri wipe ind i Lumevi Neglelakfjerner, hvorefter du placere din fnugfri wipe på neglen og klemmer den fast i 15 minutter med sølvpapir og negleklips. Fjern herefter foliet og skrab din gellak af med en neglebåndsskubber. Gentag hvis nødvendigt. Vi anbefaler negleolie efter din behandling.</p>
    <h4>ADVARSEL:</h4><p>Opbevares utilgængelig t for børn. Stop din behandling hvis følsomhed eller irritation opstår.</p>
  </div>
  <div class="info info--en"><span class="flag flag--us"></span>
    <h4>DIRECTIONS FOR USE:</h4><p>To remove the Lumevi, soak a lint free wipe with the Lumevi Polish Remover, place the saturated wipe on the nail and wrap each nail in foil for 15 minutes. Remove the foil and peel off the gel polish remover. Re-apply if needed. We recommend that you moisturise your nails after this treatment.</p>
    <h4 style="margin-top:52px">CAUTION:</h4><p>Keep out of the reach of children. Discontinue use if sensitivity or irritation occurs.</p>
  </div>
  <div class="rule"></div>
  <div class="footer">
    <p class="address">Nordhaven Studio ApS - Fjordvej 12, 2450 Copenhagen, Denmark</p>
    <p class="web">lumevi.example</p>
    <p class="made">Made in Germany</p>
    <div class="icons"><svg><use href="#icon-jar"/></svg><svg><use href="#icon-recycle"/></svg><svg><use href="#icon-warning"/></svg><svg><use href="#icon-lamp"/></svg></div>
    <div class="size">15ml e 0.5oz</div>
  </div>
</section>

</body>
</html>
```